Pause Your Day And Browse- PYDB poster

I am the Vice President of Advocacy for the Coastline Shelfkeepers Guild. I am looking to have a set of posters made for PYDB (Pause Your Day and Browse) October 23. PYDB is a time when all school children in BC are encouraged to Pause Your Day and Browse for 15-20 minutes at some point in their day.

I would like to get a set of 2 digital posters designed (if possible it would be nice to have the option to print to both 11 x 17 and 8.5 x 11 paper). We need a poster that is high school (Grade 8-12) appropriate and one that is elementary (Grade k-7) appropriate. Both posters need to be replicated in French. All posters need to have the KWNU logo on them as well as the Coastline Shelfkeepers Guild Logo.

Here is a link to last year's successful design http://kwnu-example.org/csg/info/advocacy.html
There are two additional samples in the uploaded files section.

Each poster needs to have the following information:

-Pause Your Day and Browse (PYDB)
- The date Monday, October 23, 2017
-the logo for the KWNU (attached)
-the logo for the CSG (attached)- the logos do not have to be large.

Target Market(s)

Children ages 5-12 and 12-17 as well as their teachers

Industry/Entity Type

Teacher

Font styles to use
Sans Serif

Requirements
Must have
• Must have both logos- colours may be changed for either or both
Nice to have
• Clear, Bright lettering. Images of child or children enjoying reading
Should not have
• stereotypes

```html
<!DOCTYPE html>
<html lang="en">
<head>
<meta charset="utf-8">
<title>Pause Your Day and Browse (PYDB) – Poster</title>
<link rel="stylesheet" href="https://fonts.googleapis.com/css2?family=Roboto:wght@700;900&display=swap">
<style>
  :root {
    --paper: #ffffff;
    --slate: #939598;
    --teal: #4bb3c8;
    --teal-deep: #17a3bf;
    --navy: #25408f;
    --ink: #231f20;
    --leaf: #3c9a3f;
    --sand: #e9e4d6;
    --art-fill: #f4f2ec;
  }
  html, body {
    margin: 0;
    padding: 0;
    width: 1200px;
    height: 801px;
    overflow: hidden;
    background: var(--paper);
  }
  .poster {
    position: relative;
    width: 1200px;
    height: 801px;
    background: var(--paper);
    font-family: "Roboto", Arial, sans-serif;
    overflow: hidden;
  }
  .poster__swoosh {
    position: absolute;
    inset: 0;
    width: 1200px;
    height: 801px;
  }
  .headline {
    margin: 0;
    font-weight: 900;
  }
  .headline__lead,
  .headline__rest {
    position: absolute;
    display: block;
    line-height: 1;
    white-space: nowrap;
  }
  .headline__lead {
    left: 168px;
    top: 106px;
    font-size: 182px;
    letter-spacing: -3px;
    color: var(--slate);
  }
  .headline__rest {
    left: 170px;
    font-size: 56px;
    letter-spacing: 0.5px;
    color: var(--teal);
  }
  .headline__rest--first { top: 279px; }
  .headline__rest--second { top: 346px; }
  .event-date {
    position: absolute;
    left: 170px;
    top: 409px;
    margin: 0;
    font-weight: 700;
    font-size: 38px;
    line-height: 1;
    color: var(--slate);
    white-space: nowrap;
  }
  .art-slot {
    position: absolute;
    left: 760px;
    top: 70px;
    width: 386px;
    height: 470px;
    border-radius: 12px;
    background: var(--art-fill);
  }
  .partners {
    position: absolute;
    left: 776px;
    top: 636px;
    width: 380px;
    height: 112px;
    display: flex;
    align-items: center;
    justify-content: space-between;
  }
  .partner {
    display: flex;
    flex-direction: column;
    align-items: center;
  }
  .partner--union {
    flex-direction: row;
    gap: 6px;
  }
  .partner__dot {
    width: 64px;
    height: 64px;
    border-radius: 50%;
    background: var(--navy);
  }
  .partner__name {
    font-weight: 900;
    line-height: 1;
  }
  .partner__name--union { color: var(--navy); font-size: 24px; }
  .partner__name--guild { color: var(--ink); font-size: 36px; }
  .partner__name--event { color: var(--leaf); font-size: 46px; }
  .partner__caption {
    margin-top: 5px;
    font-weight: 700;
    font-size: 7px;
    text-align: center;
    line-height: 1.2;
    text-transform: uppercase;
  }
  .partner__caption--guild { color: var(--ink); width: 86px; }
  .partner__caption--event { color: var(--leaf); width: 118px; }
</style>
</head>
<body>
  <main class="poster">
    <svg class="poster__swoosh" viewBox="0 0 1200 801" aria-hidden="true">
      <defs>
        <linearGradient id="streak-fade" x1="0" x2="1" y1="0" y2="0">
          <stop offset="0" stop-color="#7fcbdb"/>
          <stop offset="0.35" stop-color="#17a3bf"/>
          <stop offset="1" stop-color="#17a3bf"/>
        </linearGradient>
        <linearGradient id="mist-fade" x1="0" x2="1" y1="0" y2="0">
          <stop offset="0" stop-color="#dff1f6"/>
          <stop offset="1" stop-color="#ffffff" stop-opacity="0"/>
        </linearGradient>
      </defs>
      <path d="M0,640 L260,640 L300,801 L0,801 Z" fill="url(#mist-fade)"/>
      <path d="M222,0 C90,150 30,420 120,620 C165,710 235,770 290,801 L236,801 C165,735 105,655 72,565 C20,410 40,170 150,0 Z" fill="var(--teal)"/>
      <path d="M0,493 C300,505 600,535 822,564 C600,566 300,568 0,569 Z" fill="url(#streak-fade)"/>
      <path d="M0,652 C380,622 800,587 1097,567 C800,602 380,664 0,706 Z" fill="url(#streak-fade)"/>
      <path d="M640,760 C820,720 1000,700 1200,690" fill="none" stroke="var(--sand)" stroke-width="2"/>
    </svg>

    <h1 class="headline">
      <span class="headline__lead">PAUSE</span>
      <span class="headline__rest headline__rest--first">YOUR DAY AND</span>
      <span class="headline__rest headline__rest--second">BROWSE (PYDB)</span>
    </h1>
    <p class="event-date">Monday October 23, 2017</p>

    <div class="art-slot" role="img" aria-label="Illustration area"></div>

    <footer class="partners">
      <div class="partner partner--union">
        <span class="partner__dot"></span>
        <span class="partner__name partner__name--union">KWNU</span>
      </div>
      <div class="partner partner--guild">
        <span class="partner__name partner__name--guild">CSG</span>
        <span class="partner__caption partner__caption--guild">Coastline Shelfkeepers Guild</span>
      </div>
      <div class="partner partner--event">
        <span class="partner__name partner__name--event">PYDB</span>
        <span class="partner__caption partner__caption--event">Pause Your Day and Browse<br>October 23, 2017</span>
      </div>
    </footer>
  </main>
</body>
</html>
```